Professional Business Card for Luxury Hotel & Resort Development Firm. Advisory firm

Project Overview: We are a specialized advisory firm focused on Hotel & Resort Development. Our clients are high-net-worth investors and major hospitality brands.

Design Requirements:

Style: Minimalist, sophisticated, and trustworthy. We want to avoid looking too "corporate" or "dry"—it should feel premium.

Key Elements: Please incorporate our logo [もしロゴがあれば] and emphasize a clean layout with plenty of white space.

Color Palette: We prefer Grey and White or Black and White to evoke a sense of luxury and stability.

Typography: Professional garamond, or sans-serif or elegant serif fonts

Goal: The card should feel substantial and high-end when handed to a client, reflecting our expertise in multi-million dollar developments.
Updates

I am currently on a business trip for field research and have limited access to my desktop. Additionally, I have just provided detailed technical feedback to a designer and am waiting for their refined proposals. To ensure the final logo meets the high standards of my new advisory firm, I would like to extend the deadline by 7 days. Thank you for your support.

Target Market(s)

High-net-worth investors, luxury hospitality brands, and real estate developers.

Contact Information for Business Card

Firm Name: Harbor Crest Partners, My Name: Kenji Morisawa, Title: Founder, Address 5-8-4 Kitanomura Aoba Yokohama Japan 225-0143, email address: kmorisawa@harborcrestpx.example, Tel: +81 90-4183-2750. Front Site (Primary): Japanese translation of the back side, Please use a clean Japanese font (like Mincho) that complements the Garmond on the English side Back side: English. Note for Japanese text: since the frond side is the main fae, please ensure the layout is clean and professional. Please use a high-quality Mincho ( Serif-style) font for Japanese to mach the Garmond used on the English side. Text for Front side (Japanese) Harbor Crest Partners, 役職:代表、森沢健二、225-0143 横浜市青葉区北野村5-8-4. Name of the firm can stay in English.

Font styles to use
Other font styles liked:
• Font Preference: Please use Garamond for all text to maintain a consistent, elegant, and classic professional look.

Requirements
Must have
• Professional and clean layout, high-end feel.
Nice to have
• Minimalist design with subtle luxury accents.

```html
<!DOCTYPE html>
<html lang="ja">
<head>
<meta charset="utf-8">
<title>Harbor Crest Partners — Business Card</title>
<link rel="stylesheet" href="https://fonts.googleapis.com/css2?family=EB+Garamond:ital,wght@0,400;0,500;1,400&family=Shippori+Mincho:wght@400;500&display=swap">
<style>
  :root {
    --backdrop: #9b9b9b;
    --paper: #f6f6f5;
    --ink: #6b6b6b;
    --ink-strong: #5a5a5a;
    --rule: #8a8a8a;
    --shadow: rgba(0, 0, 0, 0.22);
  }
  * { margin: 0; padding: 0; box-sizing: border-box; }
  html, body {
    width: 1200px;
    height: 1001px;
    overflow: hidden;
    background: var(--backdrop);
  }
  .stage {
    width: 1200px;
    height: 1001px;
    display: flex;
    justify-content: center;
    align-items: center;
    gap: 110px;
  }
  .card {
    width: 340px;
    height: 562px;
    background: var(--paper);
    box-shadow: 0 18px 40px var(--shadow);
    color: var(--ink);
    display: flex;
    flex-direction: column;
    align-items: center;
    text-align: center;
    padding: 92px 40px 0;
    font-family: "EB Garamond", Garamond, serif;
  }
  .wordmark {
    display: flex;
    align-items: center;
    gap: 9px;
    font-family: "EB Garamond", Garamond, serif;
    font-size: 21px;
    font-weight: 400;
    color: var(--ink);
    letter-spacing: 0.02em;
  }
  .wordmark-dot {
    width: 9px;
    height: 9px;
    border-radius: 50%;
    background: var(--ink);
  }
  .rule {
    width: 232px;
    height: 1px;
    background: var(--rule);
  }

  /* Japanese face */
  .card--ja { font-family: "Shippori Mincho", "EB Garamond", serif; }
  .card--ja .identity { margin-top: 222px; }
  .card--ja .title { font-size: 15px; letter-spacing: 0.08em; }
  .card--ja .name {
    font-size: 31px;
    font-weight: 500;
    color: var(--ink-strong);
    letter-spacing: 0.06em;
    margin-top: 4px;
  }
  .card--ja .rule { margin-top: 16px; }
  .card--ja .postal {
    font-family: "EB Garamond", Garamond, serif;
    font-size: 15px;
    margin-top: 14px;
    letter-spacing: 0.04em;
  }
  .card--ja .address { font-size: 15px; margin-top: 4px; letter-spacing: 0.04em; }

  /* English face */
  .card--en .identity { margin-top: 86px; }
  .card--en .name {
    font-size: 19px;
    font-weight: 500;
    color: var(--ink-strong);
    letter-spacing: 0.04em;
    text-transform: uppercase;
  }
  .card--en .title { font-size: 15px; font-style: italic; margin-top: 2px; }
  .card--en .rule { margin-top: 14px; }
  .card--en .address { font-size: 14.5px; line-height: 1.3; margin-top: 12px; }
  .card--en .rule--second { margin-top: 12px; }
  .card--en .contact { font-size: 14px; line-height: 1.35; margin-top: 12px; }
</style>
</head>
<body>
<main class="stage">
  <section class="card card--ja" aria-label="日本語面">
    <div class="wordmark"><span class="wordmark-dot"></span>Harbor Crest Partners</div>
    <div class="identity">
      <p class="title">代表</p>
      <p class="name">森沢健二</p>
    </div>
    <div class="rule"></div>
    <p class="postal">225-0143</p>
    <p class="address">横浜市青葉区北野村<span style="font-family:'EB Garamond',serif">5-8-4</span></p>
  </section>

  <section class="card card--en" aria-label="English side" lang="en">
    <div class="wordmark"><span class="wordmark-dot"></span>Harbor Crest Partners</div>
    <div class="identity">
      <p class="name">Kenji Morisawa</p>
      <p class="title">Founder</p>
    </div>
    <div class="rule"></div>
    <p class="address">5-8-4 Kitanomura,<br>Aoba,<br>Yokohama Japan 225-0143</p>
    <div class="rule rule--second"></div>
    <p class="contact">kmorisawa@harborcrestpx.example<br>+81 90-4183-2750</p>
  </section>
</main>
</body>
</html>
```